Marwick Business finance web design

We are a newly established business which provides invoice finance to Small Businesses in England and Wales.
Our approach is very much a funder where the small business owner can talk to the decision maker. We will guarantee on receipt of information, a decision within 24 hours.
We are not a bank so the look of the website need to be friendly but professional.
Have two types of people we are trying to attract to the website: 1) partners who are small business owners and 2) introducers who is accountants and commercial brokers who introduce us to the small businesses.
Currently no website, although domain has been reserved.
The design should be:
Professional
“Clean” Look
Designed to convey Trust and Authority.
Appeal to the small business owner.
Must incorporate:
Logo (attached)
Front page:Top tabs to other pages 1) About us 2) Services 3) Introducers 4) Contact us
Need picture and logo on page.
1) About us page- Room for talk about the company, the people and our critera.
2) Services page- We need for what invoice finance is, and 5 boxes for different services we will provide. (link on page to contact us)
3) Introducers page- We need a part for why become an introducer? Who we can help? Why we are different? (link on page to contact us)
4) Contact us page- Office address, email, tel and if possible a map and a contact me part which will email direct to us.
Text will be provided for the design, if we can see the setup of the website we will provide a part for each of the pages to support.
Styles we think convey the correct image:
www.tovelfunding.example
www.brimsorkfs.example
www.plyfunding.example
Target Market(s)
Small business owners
Industry/Entity Type
Finance
Number of Pages Required
5+ page
Look and feel

```html
<!DOCTYPE html>
<html lang="en">
<head>
<meta charset="utf-8">
<title>Marwick Business Finance</title>
<link href="https://fonts.googleapis.com/css2?family=Roboto:wght@300;400;500;700&display=swap" rel="stylesheet">
<style>
:root{
  --red:#e1333b;
  --red-dark:#c92730;
  --ink:#2b2b2b;
  --text:#7a7a7a;
  --line:#d9d9d9;
  --white:#ffffff;
  --mist:#e9edf1;
  --sky:#c9dcea;
}
*{box-sizing:border-box;margin:0;padding:0}
html,body{width:1200px;height:2917px;overflow:hidden;background:var(--white)}
body{position:relative;font-family:'Roboto',Arial,sans-serif;color:var(--ink)}
.abs{position:absolute}
.section-title{position:absolute;left:0;width:1200px;text-align:center;font-size:42px;font-weight:400;color:var(--ink);letter-spacing:.5px}
.section-title span{color:var(--red)}
.lead{position:absolute;text-align:center;font-size:14px;line-height:27px;color:var(--text)}
.btn{position:absolute;background:var(--red);color:var(--white);border-radius:30px;font-size:20px;text-align:center;font-weight:400;letter-spacing:.5px}

/* hero */
.hero{left:0;top:0;width:1200px;height:680px;background:radial-gradient(circle at 70% 45%,#a9c9df 0,#d6e5ef 28%,#eef3f7 55%,#f6f8fa 100%)}
.hero-phone{right:48px;top:28px;display:flex;align-items:center;gap:14px;font-size:29px;color:var(--ink)}
.hero-phone .ring{width:66px;height:66px;border:2px solid var(--red);border-radius:50%;display:flex;align-items:center;justify-content:center;background:var(--white)}
.brand{left:0;top:190px;width:1200px;text-align:center;color:var(--ink);font-weight:700}
.brand-name{font-size:150px;line-height:150px;letter-spacing:-2px}
.brand-sub{font-size:28px;letter-spacing:1px;margin-top:6px}
.nav{left:0;top:611px;width:1200px;height:66px;border-top:1px solid #5b6670;background:rgba(255,255,255,.55)}
.nav a{position:absolute;top:0;height:66px;line-height:66px;font-size:17px;color:var(--ink);text-decoration:none;text-align:center}
.nav a.active{border-top:5px solid var(--red);line-height:56px;color:#3a5b75}
.nav-band{left:0;top:677px;width:1200px;height:10px;background:var(--red)}
.nav-notch{left:582px;top:686px}
.nav-shadow{left:40px;top:687px;width:1120px;height:60px;background:radial-gradient(ellipse at 50% 0,rgba(0,0,0,.18),rgba(0,0,0,0) 70%)}

/* services */
.services{left:0;top:1076px;width:1200px;height:496px;background:linear-gradient(135deg,#b8bcc2,#dcdfe3 45%,#eceef0)}
.card{position:absolute;top:1206px;width:249px;height:228px}
.card .photo{width:249px;height:165px}
.card .label{height:63px;background:var(--red);color:var(--white);font-size:21px;line-height:63px;padding-left:14px;position:relative}
.card .label svg{position:absolute;right:14px;top:24px}

/* introducers */
.intro{position:absolute;top:1716px;width:510px;height:146px}
.intro .photo{position:absolute;left:0;top:0;width:208px;height:146px;border:1px solid var(--line)}
.intro h3{position:absolute;left:230px;top:0;font-size:18px;font-weight:400;color:var(--ink);letter-spacing:.5px}
.intro p{position:absolute;left:230px;top:32px;width:280px;font-size:14px;line-height:29px;color:var(--text)}
.intro .more{position:absolute;left:230px;top:120px;font-size:15px;font-weight:500;color:var(--red);display:flex;align-items:center;gap:10px}

/* testimonial */
.testimonial{left:0;top:1926px;width:1200px;height:311px;background:linear-gradient(120deg,#f4f5f6,#e3e6e9 55%,#d9dde1)}
.avatar{left:160px;top:2024px;width:128px;height:128px;border-radius:50%;border:5px solid var(--white);background:radial-gradient(circle at 50% 40%,#d9b9a2,#7a5a48 70%);box-shadow:0 2px 6px rgba(0,0,0,.2)}
.quote-title{left:314px;top:1980px;font-size:40px;font-weight:400}
.quote-title span{color:var(--red)}
.quote{left:316px;top:2044px;width:770px;font-size:15px;line-height:27px;color:#555}
.quote-name{left:316px;top:2148px;font-size:15px;color:var(--red)}

/* contact */
.field{position:absolute;height:52px;border:1px solid var(--line);font-size:15px;color:#666;padding:14px 10px;background:var(--white)}
.field.focus{border-color:var(--red);color:var(--red)}

/* footer */
.footer{left:0;top:2707px;width:1200px;height:210px;background:var(--red);color:var(--white)}
.footer-nav a{position:absolute;top:2744px;font-size:15px;color:var(--white);text-decoration:none}
.footer-nav a.pill{left:78px;top:2728px;width:96px;height:46px;border:2px solid var(--white);border-radius:24px;text-align:center;line-height:42px}
.social{position:absolute;top:2728px;width:48px;height:48px;border-radius:50%}
.footer-rule{left:78px;top:2797px;width:1044px;height:1px;background:rgba(255,255,255,.35)}
.footer-head{left:80px;top:2808px;font-size:18px;font-weight:500;letter-spacing:.5px}
.info{position:absolute;top:2838px;display:flex;align-items:center;gap:16px;font-size:14px;line-height:25px}
.info .dot{width:50px;height:50px;border-radius:50%;display:flex;align-items:center;justify-content:center;flex:none}
.info .dot.solid{background:var(--white)}
.info .dot.line{border:2px solid var(--white)}
</style>
</head>
<body>

<!-- Hero -->
<div class="abs hero" role="img" aria-label="Soft blue photograph of a glass globe resting on financial charts"></div>
<div class="abs hero-phone">
  <span class="ring"><svg width="30" height="30" viewBox="0 0 24 24"><path fill="#e1333b" d="M6.6 10.8a15 15 0 0 0 6.6 6.6l2.2-2.2a1 1 0 0 1 1-.25 11.4 11.4 0 0 0 3.6.57 1 1 0 0 1 1 1V20a1 1 0 0 1-1 1A17 17 0 0 1 3 4a1 1 0 0 1 1-1h3.5a1 1 0 0 1 1 1c0 1.25.2 2.45.57 3.57a1 1 0 0 1-.25 1z"/></svg></span>
  <span>123 456 7890</span>
</div>
<div class="abs brand">
  <div class="brand-name">Marwick</div>
  <div class="brand-sub">BUSINESS FINANCE LIMITED</div>
</div>
<nav class="abs nav">
  <a class="active" href="#" style="left:216px;width:78px">HOME</a>
  <a href="#" style="left:348px;width:104px">ABOUT US</a>
  <a href="#" style="left:510px;width:100px">SERVICES</a>
  <a href="#" style="left:668px;width:124px">INTRODUCERS</a>
  <a href="#" style="left:852px;width:118px">CONTACT US</a>
</nav>
<div class="abs nav-shadow"></div>
<div class="abs nav-band"></div>
<svg class="abs nav-notch" width="36" height="20" viewBox="0 0 36 20"><path d="M0 0h36L18 20z" fill="#e1333b"/></svg>

<!-- Welcome -->
<h1 class="section-title" style="top:752px">WELCOME TO <span>MARWICK</span></h1>
<p class="lead" style="left:140px;top:812px;width:920px">Lorem Ipsum is simply dummy text of the printing and typesetting industry. Lorem Ipsum has been the industry's standard dummy text ever since the 1500s, when an unknown printer took a galley of type and scrambled it to make a type specimen book.<br>It has survived not only five centuries. Lorem Ipsum is simply dummy text of the printing and typesetting industry. Lorem Ipsum has been the industry's standard dummy text ever since the 1500s, when an unknown printer took a galley of type and scrambled it to make a type specimen book. It has survived not only five centuries.</p>
<a class="btn" style="left:512px;top:958px;width:177px;height:57px;line-height:57px">KNOW MORE</a>

<!-- Services -->
<div class="abs services" role="img" aria-label="Faded photograph of a calculator and financial paperwork"></div>
<h2 class="section-title" style="top:1132px">OUR <span>SERVICES</span></h2>
<div class="card" style="left:78px"><div class="photo" role="img" aria-label="Green rising bar chart on a grid" style="background:linear-gradient(160deg,#f2f4f2,#9ccf7e 60%,#4e9a3c)"></div><div class="label">SERVICES ONE<svg width="18" height="16" viewBox="0 0 18 16"><path d="M2 2l6 6-6 6M9 2l6 6-6 6" stroke="#fff" stroke-width="2.4" fill="none"/></svg></div></div>
<div class="card" style="left:342px"><div class="photo" role="img" aria-label="Business people meeting in a bright office" style="background:linear-gradient(160deg,#e8f1f8,#8fb3cf 55%,#34506a)"></div><div class="label">SERVICES TWO<svg width="18" height="16" viewBox="0 0 18 16"><path d="M2 2l6 6-6 6M9 2l6 6-6 6" stroke="#fff" stroke-width="2.4" fill="none"/></svg></div></div>
<div class="card" style="left:607px"><div class="photo" role="img" aria-label="Calculator and pen on a financial chart" style="background:linear-gradient(160deg,#5a7fb8,#9fb7d8 50%,#e4ecf5)"></div><div class="label">SERVICES THREE<svg width="18" height="16" viewBox="0 0 18 16"><path d="M2 2l6 6-6 6M9 2l6 6-6 6" stroke="#fff" stroke-width="2.4" fill="none"/></svg></div></div>
<div class="card" style="left:873px"><div class="photo" role="img" aria-label="Stacks of gold coins" style="background:linear-gradient(160deg,#f1efe9,#d9b25a 55%,#8a6420)"></div><div class="label">SERVICES FOUR<svg width="18" height="16" viewBox="0 0 18 16"><path d="M2 2l6 6-6 6M9 2l6 6-6 6" stroke="#fff" stroke-width="2.4" fill="none"/></svg></div></div>
<a class="btn" style="left:519px;top:1453px;width:162px;height:56px;line-height:56px">VIEW ALL</a>

<!-- Introducers -->
<h2 class="section-title" style="top:1624px">OUR <span>INTRODUCERS</span></h2>
<div class="intro" style="left:78px">
  <div class="photo" role="img" aria-label="Two businessmen shaking hands" style="background:linear-gradient(120deg,#cfd6dc,#5b6470 60%,#2f343a)"></div>
  <h3>WHO WE HELP ?</h3>
  <p>Lorem Ipsum is simply text of dummy text of the printing and type setting is simply text of dummy text of print..</p>
  <span class="more">READ MORE... <svg width="14" height="12" viewBox="0 0 18 16"><path d="M2 2l6 6-6 6M9 2l6 6-6 6" stroke="#e1333b" stroke-width="2.4" fill="none"/></svg></span>
</div>
<div class="intro" style="left:606px">
  <div class="photo" role="img" aria-label="Calculator and cheque on a desk" style="background:linear-gradient(120deg,#8eaac4,#d7dee4 55%,#f1efe8)"></div>
  <h3>WHY WE ARE DIFFERENT ?</h3>
  <p>Lorem Ipsum is simply text of dummy text of the printing and type setting is simply text of dummy text of print..</p>
  <span class="more">READ MORE... <svg width="14" height="12" viewBox="0 0 18 16"><path d="M2 2l6 6-6 6M9 2l6 6-6 6" stroke="#e1333b" stroke-width="2.4" fill="none"/></svg></span>
</div>

<!-- Testimonial -->
<div class="abs testimonial" role="img" aria-label="Faded photograph of a hand writing over documents"></div>
<svg class="abs" style="left:76px;top:2060px" width="24" height="48" viewBox="0 0 24 48"><path d="M22 2L2 24l20 22" stroke="#9a9a9a" stroke-width="1.5" fill="none"/></svg>
<svg class="abs" style="left:1058px;top:2060px" width="24" height="48" viewBox="0 0 24 48"><path d="M2 2l20 22L2 46" stroke="#9a9a9a" stroke-width="1.5" fill="none"/></svg>
<div class="abs avatar" role="img" aria-label="Portrait photograph of a client"></div>
<h2 class="abs quote-title">WHAT OUR <span>CLIENT SAY</span></h2>
<p class="abs quote">Lorem Ipsum is simply dummy text of the printing and typesetting industry. Lorem Ipsum has been the industry's standard dummy text ever since the 1500s, when an unknown printer took a galley of type and scrambled it to make a type specimen book. It has survived not only five centuries.</p>
<span class="abs quote-name">CLIENT NAME</span>

<!-- Contact -->
<h2 class="section-title" style="top:2290px">CONTACT <span>US</span></h2>
<p class="lead" style="left:160px;top:2346px;width:880px">Lorem Ipsum is simply dummy text of the printing and typesetting industry. Lorem Ipsum has been the industry's standard dummy text ever since the 1500s, when an unknown printer took a galley of type and scrambled it to make a type specimen book.</p>
<div class="field focus" style="left:154px;top:2414px;width:292px">Name*</div>
<div class="field" style="left:455px;top:2414px;width:292px">Email*</div>
<div class="field" style="left:757px;top:2414px;width:291px">Phone*</div>
<div class="field" style="left:154px;top:2474px;width:894px;height:104px">Message*</div>
<a class="btn" style="left:517px;top:2591px;width:167px;height:56px;line-height:56px">SUBMIT</a>

<!-- Footer -->
<footer class="abs footer"></footer>
<div class="footer-nav">
  <a class="pill" href="#">Home</a>
  <a href="#" style="left:208px">About Us</a>
  <a href="#" style="left:310px">Services</a>
  <a href="#" style="left:408px">Introducers</a>
  <a href="#" style="left:516px">Contact Us</a>
</div>
<span class="social" style="left:964px;background:var(--white)" aria-label="Social profile"></span>
<span class="social" style="left:1020px;border:2px solid var(--white)" aria-label="Social profile"></span>
<span class="social" style="left:1076px;border:2px solid var(--white)" aria-label="Social profile"></span>
<div class="abs footer-rule"></div>
<div class="abs footer-head">GET IN TOUCH</div>
<div class="info" style="left:78px;color:#fff">
  <span class="dot solid"><svg width="22" height="28" viewBox="0 0 24 30"><path d="M12 0C5.4 0 0 5.3 0 11.8 0 20 12 30 12 30s12-10 12-18.2C24 5.3 18.6 0 12 0zm0 16a4.5 4.5 0 1 1 0-9 4.5 4.5 0 0 1 0 9z" fill="#e1333b"/></svg></span>
  <span>101 - Lorem ipsum is the<br>simple dummy text.</span>
</div>
<div class="info" style="left:343px;color:#fff">
  <span class="dot line"><svg width="22" height="22" viewBox="0 0 24 24"><path fill="#fff" d="M6.6 10.8a15 15 0 0 0 6.6 6.6l2.2-2.2a1 1 0 0 1 1-.25 11.4 11.4 0 0 0 3.6.57 1 1 0 0 1 1 1V20a1 1 0 0 1-1 1A17 17 0 0 1 3 4a1 1 0 0 1 1-1h3.5a1 1 0 0 1 1 1c0 1.25.2 2.45.57 3.57a1 1 0 0 1-.25 1z"/></svg></span>
  <span>123 456 7890</span>
</div>
<div class="info" style="left:607px;color:#fff">
  <span class="dot line"><svg width="24" height="18" viewBox="0 0 24 18"><rect x="1" y="1" width="22" height="16" rx="2" fill="#fff"/><path d="M1 2l11 8 11-8" stroke="#e1333b" stroke-width="1.8" fill="none"/></svg></span>
  <span>info@marwick.example</span>
</div>
<div class="info" style="left:876px;color:#fff">
  <span>© 2016 MARWICK - All rights<br>reserved.</span>
</div>

</body>
</html>
```